FERNGLOW website contest - Make it colorful

Beauty salon focusing on microblading need a better website template. Please make a 1 page site mobile optimized and nicer layout with better color formulation. Would love interactive images in the site. You can use stock images and if approve we can pay for it.
Current site:
teskafernglow.com

Inspiration:
https://pixelvane.com/shots/48127093-Microblading-HomePage
https://pixelvane.com/shots/7164920-Lumetti-Microblading-Eyebrow-Beauty-Salon-Pagenest-Theme

Target Market(s)

women

Industry/Entity Type

beauty salon

Number of Pages Required

1 page

Font styles to use
Serif
Decorative
Script

Requirements
Nice to have
• As pretty as possible

```html
<!DOCTYPE html>
<html lang="en">
<head>
<meta charset="utf-8">
<title>Atelier of brows by Teska</title>
<link href="https://fonts.googleapis.com/css2?family=Gilda+Display&family=Montserrat:wght@400;500;600&display=swap" rel="stylesheet">
<style>
  :root {
    --page: #f6f6f6;
    --white: #ffffff;
    --ink: #2e2e33;
    --muted: #5c5c63;
    --rose: #ec6f8c;
    --rose-btn: #ef8098;
    --blush: #eebdca;
    --mist: #e8eaeb;
    --card-line: #f3cdd6;
  }
  * { box-sizing: border-box; margin: 0; padding: 0; }
  html, body { width: 1200px; height: 800px; overflow: hidden; background: var(--page); }
  body { font-family: "Montserrat", sans-serif; color: var(--ink); position: relative; }

  .site-nav {
    height: 84px; background: var(--white);
    display: flex; align-items: center; padding: 0 64px 0 86px;
  }
  .brand { font-family: "Gilda Display", serif; color: var(--rose); font-size: 21px; letter-spacing: 0.5px; }
  .nav-links { display: flex; list-style: none; gap: 27px; margin-left: 46px; align-items: center; }
  .nav-links li { font-size: 10.5px; font-weight: 500; color: var(--muted); letter-spacing: 0.2px; }
  .nav-links li.is-active { color: var(--rose); }
  .cart-btn {
    margin-left: 18px; background: var(--rose-btn); color: var(--white);
    font-size: 10.5px; font-weight: 500; padding: 11px 25px; border-radius: 3px;
  }

  .hero { position: relative; height: 476px; overflow: hidden; background: var(--page); }
  .hero-shapes { position: absolute; inset: 0; }
  .hero-copy { position: absolute; left: 96px; top: 112px; }
  .hero-kicker { font-family: "Gilda Display", serif; color: var(--rose); font-size: 14px; }
  .hero-title { font-family: "Gilda Display", serif; font-weight: 400; font-size: 52px; line-height: 48px; margin-top: 22px; color: var(--ink); }
  .hero-title .accent { color: var(--rose); }
  .hero-sub { font-size: 13px; color: var(--muted); margin-top: 22px; }
  .hero-actions { display: flex; gap: 14px; margin-top: 34px; }
  .btn { font-size: 12px; font-weight: 600; letter-spacing: 0.6px; height: 38px; display: inline-flex; align-items: center; justify-content: center; border-radius: 3px; }
  .btn-solid { background: var(--rose-btn); color: var(--white); width: 120px; }
  .btn-outline { border: 1.5px solid var(--rose-btn); color: var(--rose); background: var(--white); width: 144px; }

  .care { padding: 32px 96px 0; }
  .care-title { font-family: "Gilda Display", serif; font-weight: 400; font-size: 33px; line-height: 40px; }
  .care-sub { font-size: 12.5px; color: var(--muted); margin-top: 6px; padding-left: 6px; }
  .features { display: flex; gap: 24px; margin-top: 20px; }
  .feature {
    flex: 1; height: 108px; background: var(--white);
    border: 1px solid var(--card-line); border-radius: 4px; padding: 20px 26px;
  }
  .feature.is-featured { border: 2px solid var(--rose-btn); padding: 19px 25px; }
  .feature-head { border-left: 4px solid var(--rose); padding-left: 12px; }
  .feature-head h3 { font-family: "Gilda Display", serif; font-weight: 400; font-size: 19px; line-height: 22px; }
  .feature-head p { font-family: "Gilda Display", serif; font-size: 14px; line-height: 18px; color: var(--ink); }
  .feature-text { font-size: 10.5px; line-height: 15px; color: var(--muted); margin-top: 12px; }
</style>
</head>
<body>
  <header class="site-nav">
    <div class="brand">FERNGLOW</div>
    <ul class="nav-links">
      <li class="is-active">HOME</li>
      <li>ABOUT</li>
      <li>SERVICES</li>
      <li>GALLERY</li>
      <li>SHOP</li>
      <li>ACADEMY</li>
      <li>CONTACT US</li>
      <li>CUSTOMER FEEDBACK</li>
      <li>MORE</li>
    </ul>
    <span class="cart-btn">CART</span>
  </header>

  <section class="hero">
    <svg class="hero-shapes" width="1200" height="476" viewBox="0 0 1200 476">
      <defs>
        <linearGradient id="portraitTone" x1="0" y1="0" x2="1" y2="1">
          <stop offset="0" stop-color="#e3c9a8"/>
          <stop offset="0.55" stop-color="#ecc4b4"/>
          <stop offset="1" stop-color="#e6a9b2"/>
        </linearGradient>
      </defs>
      <path d="M465 0 C 540 110, 640 170, 650 270 C 656 360, 600 430, 540 476 L1200 476 L1200 0 Z" fill="var(--blush)"/>
      <path d="M0 138 C 210 80, 470 190, 540 476 L0 476 Z" fill="var(--mist)"/>
      <rect x="590" y="24" width="420" height="452" rx="200" ry="200" fill="url(#portraitTone)" role="img" aria-label="Portrait of a woman with long blonde hair resting her hands near her face and shoulder"/>
    </svg>
    <div class="hero-copy">
      <div class="hero-kicker">Fernglow Brow Studio</div>
      <h1 class="hero-title">Atelier of <span class="accent">brows</span><br>by Teska</h1>
      <p class="hero-sub">Your personal eyebrow specialist.</p>
      <div class="hero-actions">
        <span class="btn btn-solid">TRY NOW</span>
        <span class="btn btn-outline">VIEW SHOP</span>
      </div>
    </div>
  </section>

  <section class="care">
    <h2 class="care-title">Your Eyebrows and Beauty</h2>
    <p class="care-sub">Let us take care of it.</p>
    <div class="features">
      <article class="feature">
        <div class="feature-head"><h3>Licensed</h3><p>Microblading artist</p></div>
        <p class="feature-text">License from various states in United States.</p>
      </article>
      <article class="feature is-featured">
        <div class="feature-head"><h3>Years</h3><p>of experience</p></div>
        <p class="feature-text">Over thousands of cases. Oversea study and practice.</p>
      </article>
      <article class="feature">
        <div class="feature-head"><h3>European</h3><p>latest technique</p></div>
        <p class="feature-text">We study European-style natural hair flow, improve and make it suitable for Asians.</p>
      </article>
    </div>
  </section>
</body>
</html>
```